Bramwell Dental personal information forms

We are a Dental Practice that require an update to our information forms, there are 3 versions of it.
I will attach our old ones, we need to keep the same information on there, we just want them to look better and use our current logo and colours.
Our website is www.bramwelldental-example.net
Our facebook is www.facebook.com/bramwelldentalkestonwalk/
..................................................................................................

Target Market(s)

Everyone, easy to read

Industry/Entity Type

Dental Clinic

Colors
0692cd
34a6d7
cee9f5
ffffff
0255a3
3276b5

Requirements
Must have
• Logo
• Our colours
• same information as the uploaded versions
Should not have
• any other colour besides the blues, black and white

```html
<!DOCTYPE html>
<html lang="en">
<head>
<meta charset="utf-8">
<title>Bramwell Dental – Medical History Update</title>
<link href="https://fonts.googleapis.com/css2?family=Roboto+Condensed:ital,wght@0,400;0,700;1,400&family=Roboto+Slab:wght@700&display=swap" rel="stylesheet">
<style>
:root{
  --blue:#0692cd;
  --blue-mid:#34a6d7;
  --blue-pale:#cee9f5;
  --navy:#0255a3;
  --blue-steel:#3276b5;
  --white:#ffffff;
  --ink:#111111;
  --field-top:#f4f5f6;
  --field-bottom:#c9cbcd;
  --field-edge:#b9bcbf;
  --backdrop:#e8edf1;
}
*{margin:0;padding:0;box-sizing:border-box}
html,body{width:974px;height:1200px;overflow:hidden;background:var(--backdrop)}
.form{position:absolute;left:63px;top:0;width:848px;height:1200px;background:var(--white);font-family:"Roboto Condensed",sans-serif;color:var(--ink)}
.header-shape{position:absolute;left:0;top:0}
.brand{position:absolute;left:20px;width:314px;top:66px;text-align:center;color:var(--white);font-size:40px;font-weight:400;line-height:1;letter-spacing:.5px}
.surgeons{position:absolute;left:360px;width:440px;text-align:center;font-weight:700;line-height:1}
.surgeons .names{position:absolute;left:0;width:100%;top:22px;font-size:28px;color:var(--blue-pale)}
.surgeons .title{position:absolute;left:0;width:100%;top:58px;font-size:28px;color:var(--white)}
.welcome{position:absolute;left:380px;width:430px;top:151px;text-align:center;font-family:"Roboto Slab",serif;font-weight:700;font-size:33px;color:var(--navy)}
.sticker{position:absolute;left:466px;top:203px;width:257px;height:52px;border-radius:26px;background:linear-gradient(var(--field-top),var(--field-bottom));border:1px solid var(--field-edge);display:flex;align-items:center;justify-content:center;font-style:italic;font-size:16px;color:var(--navy)}
.intro{position:absolute;left:21px;width:806px;top:284px;font-size:18px;line-height:24px;text-align:justify}
.q{position:absolute;left:21px;width:806px;font-size:15.5px;line-height:20px;display:flex;justify-content:space-between}
.yn{color:var(--blue-steel);font-weight:700;font-size:16px}
.field{position:absolute;left:21px;width:806px;height:33px;border-radius:17px;background:linear-gradient(var(--field-top),var(--field-bottom));border:1px solid var(--field-edge)}
.conditions{position:absolute;top:558px;left:0;width:848px;font-size:16px;line-height:22.8px}
.conditions ul{position:absolute;top:0;list-style:none}
.conditions li{display:flex;align-items:center}
.conditions li::before{content:"";width:11px;height:11px;margin-right:9px;border:1px solid #b8b8b8;background:linear-gradient(#f2f2f2,#d6d6d6)}
.declaration{position:absolute;left:21px;width:806px;top:1065px;font-size:15.5px;line-height:19px}
.sign{position:absolute;left:21px;width:806px;top:1124px;font-size:15.5px;line-height:20px}
.sign .line{position:absolute;top:14px;border-bottom:1.5px dashed #555}
.sign .date{position:absolute;left:588px;top:0}
.band-dark{position:absolute;left:0;top:1161px;width:848px;height:13px;background:var(--navy)}
.band-light{position:absolute;left:0;top:1174px;width:848px;height:26px;background:var(--blue-mid)}
</style>
</head>
<body>
<main class="form">
  <svg class="header-shape" width="848" height="200" viewBox="0 0 848 200" aria-hidden="true">
    <polygon points="0,108 189,179 365,110 848,110 848,128 365,128 189,198 0,131" fill="#cee9f5"/>
    <polygon points="0,0 848,0 848,110 365,110 189,179 0,108" fill="#34a6d7"/>
  </svg>
  <div class="brand">Bramwell Dental</div>
  <div class="surgeons">
    <div class="names">Dr. Martin Kovalis &amp; Dr. Owen Hartley</div>
    <div class="title">DENTAL SURGEONS</div>
  </div>

  <h1 class="welcome">Welcome back to our practice</h1>
  <div class="sticker">Affix patient sticker here</div>

  <p class="intro">THIS INFORMATION IS CONFIDENTIAL and is necessary to enable us to offer you THE BEST POSSIBLE CARE. It is now mandatory to have a written updated medical history every 2 years and we would appreciate your time in thoroughly completing this form.</p>

  <div class="q" style="top:368px"><span>Are you currently or have you taken any prescribed medication or dietary supplements in the last 12 months?</span><span class="yn">YES / NO</span></div>
  <div class="field" style="top:401px"></div>

  <div class="q" style="top:448px"><span>Allergies / Reactions ? If YES, please list below</span><span class="yn">YES / NO</span></div>
  <div class="field" style="top:476px"></div>

  <div class="q" style="top:525px"><span>Have you ever had or are you suffering from any of the following? Please tick any that apply:</span></div>
  <div class="conditions">
    <ul style="left:52px">
      <li>Rheumatic fever</li><li>Epilepsy</li><li>Asthma</li><li>Tubersulosis</li><li>Radiation Therapy</li><li>Dizziness, Fainting</li><li>Hepatitis A B or C</li><li>Recent Eye Surgery</li>
    </ul>
    <ul style="left:369px">
      <li>Diabetes</li><li>Kidney Disease</li><li>Heart Attack</li><li>High Blood Pressure</li><li>Bleeding problems</li><li>Artificial joints</li><li>Respiratory problems</li>
    </ul>
    <ul style="left:679px">
      <li>HIV Positive</li><li>High cholesterol</li><li>Cancer</li><li>Pace-maker</li><li>Osteoporosis</li><li>Heart rate problems</li><li>Heart murmur</li>
    </ul>
  </div>

  <div class="q" style="top:754px"><span>Do you have any disease, condition or problem not listed above?</span><span class="yn">YES / NO</span></div>
  <div class="field" style="top:781px"></div>

  <div class="q" style="top:829px"><span>Have you had surgery or been to hospital in the last 5 years? (if YES, please give details)</span><span class="yn">YES / NO</span></div>
  <div class="field" style="top:859px"></div>

  <div class="q" style="top:909px"><span>For Women : Are you pregnant? If yes, how many months?</span><span class="yn">YES / NO</span></div>
  <div class="field" style="top:938px"></div>

  <div class="q" style="top:985px"><span>Do you currently or have you ever smoked?</span><span class="yn">YES / NO</span></div>
  <div class="field" style="top:1015px"></div>

  <p class="declaration">The information that I have provided is to the best of my knowledge true and correct and I understand that it is my responsiibility to inform of any change in my medical status.</p>

  <div class="sign">
    <span>Patient / Parent / Person Responsible Signature :</span>
    <span class="line" style="left:323px;width:198px"></span>
    <span class="date">Date:</span>
    <span class="line" style="left:627px;width:179px"></span>
  </div>

  <div class="band-dark"></div>
  <div class="band-light"></div>
</main>
</body>
</html>
```